Business card for a gourmet fruit and vegetable retail store

Please design a business card for our boutique gourmet fruit and vegetable food store using attached logo design, with the colour options of white, black and lime green. We would like it to be unique and classic, with a large image of the logo on the back of the business card, and the business card details plus a design on the front.

Target Market(s)

High income earners in an affluent Melbourne suburb who value high quality products and done mind paying for it

Industry/Entity Type

Retail

Contact Information for Business Card

Business name: Harwick's Fine Food Merchant
Address: 27 Plumtree Rd, Kelsby VIC 3158
Name: TBC
Position Title: Director
Phone Number: TBC
Mobile: TBC

Business name is: Harwick's Fine Food Merchant. Please allow space for us to fill in the business address, contact number, person's name, position Title and mobile number.

Colors
acd036

Requirements
Must have
• The logo must have our business logo on the back, and our business details and contact details on the front. It must include the colours of white, black and lime green
Nice to have
• It can have different background colours on the front and on the back.
Should not have
• It should not have any other colours aside from white, black and lime green

```html
<!DOCTYPE html>
<html lang="en">
<head>
<meta charset="utf-8">
<title>Harwick's Fine Food Merchant – Business Card Front</title>
<link href="https://fonts.googleapis.com/css2?family=Josefin+Slab:wght@400;600&display=swap" rel="stylesheet">
<style>
  :root {
    --card-white: #ffffff;
    --ink-black: #1a1a1a;
    --lime: #acd036;
    --lime-soft: #e6f1c3;
    --pattern-grey: #ececec;
    --pattern-grey-soft: #f6f6f6;
  }
  html, body {
    margin: 0;
    padding: 0;
    width: 1200px;
    height: 792px;
    overflow: hidden;
    background: var(--card-white);
  }
  .card {
    position: relative;
    width: 1200px;
    height: 792px;
    background: var(--card-white);
    overflow: hidden;
    font-family: "Josefin Slab", Georgia, serif;
    color: var(--ink-black);
  }
  .produce-pattern {
    position: absolute;
    top: 0;
    height: 792px;
  }
  .produce-pattern--left {
    left: 0;
    width: 430px;
    background:
      radial-gradient(ellipse 170px 150px at 110px 130px, var(--pattern-grey) 0%, transparent 100%),
      radial-gradient(ellipse 190px 170px at 200px 470px, var(--pattern-grey) 0%, transparent 100%),
      radial-gradient(ellipse 160px 130px at 90px 700px, var(--pattern-grey-soft) 0%, transparent 100%),
      var(--card-white);
  }
  .produce-pattern--right {
    right: 0;
    width: 300px;
    background:
      radial-gradient(ellipse 150px 190px at 180px 150px, var(--pattern-grey) 0%, transparent 100%),
      radial-gradient(ellipse 150px 200px at 170px 560px, var(--pattern-grey) 0%, transparent 100%),
      var(--card-white);
  }
  .brand-mark {
    position: absolute;
    left: 503px;
    top: 92px;
    width: 190px;
    height: 158px;
    background: radial-gradient(ellipse at 50% 55%, var(--lime) 0%, var(--lime-soft) 75%);
    border-radius: 6px;
  }
  .brand-rule {
    position: absolute;
    left: 388px;
    top: 253px;
    width: 432px;
    height: 2px;
    background: var(--ink-black);
  }
  .brand {
    position: absolute;
    left: 0;
    right: 0;
    top: 280px;
    text-align: center;
  }
  .brand__name {
    margin: 0;
    font-size: 64px;
    font-weight: 600;
    letter-spacing: 0.15em;
    line-height: 1;
    padding-left: 0.15em;
  }
  .brand__tagline {
    margin: 14px 0 0;
    font-size: 25px;
    font-weight: 600;
    letter-spacing: 0.2em;
    line-height: 1;
    padding-left: 0.2em;
  }
  .contact {
    position: absolute;
    left: 0;
    right: 0;
    top: 443px;
    margin: 0;
    padding: 0;
    list-style: none;
    text-align: center;
    font-size: 45px;
    font-weight: 400;
    line-height: 51px;
  }
  .contact__address {
    margin-top: 10px;
    font-size: 49px;
  }
</style>
</head>
<body>
  <main class="card">
    <div class="produce-pattern produce-pattern--left" role="img" aria-label="Faint line pattern of fresh produce, a preserve jar and an apple"></div>
    <div class="produce-pattern produce-pattern--right" role="img" aria-label="Faint line pattern of fresh produce and a wedge of cheese"></div>

    <div class="brand-mark" role="img" aria-label="Line illustration of a jar, beetroot, apple and cheese"></div>
    <div class="brand-rule"></div>

    <header class="brand">
      <h1 class="brand__name">HARWICK'S</h1>
      <p class="brand__tagline">FINE FOOD MERCHANT</p>
    </header>

    <ul class="contact">
      <li class="contact__name">Name:</li>
      <li class="contact__title">Position Title: Director</li>
      <li class="contact__mobile">Mobile:</li>
      <li class="contact__phone">Phone Number:</li>
      <li class="contact__address">27 Plumtree Rd, Kelsby VIC 3158</li>
    </ul>
  </main>
</body>
</html>
```